Ayurvedic Beauty Company in Need of Business Cards

My company is a high-end ayurvedic beauty brand. I need a business card that represents that. The designer should utilize logo and color palette. I want these cards to be printed with the foil accents so keep that in mind.

I have attached the ai of my logo and business card info. As well as, some of the product we are launching soon, they do not have to be on the card.

Be creative and have fun.

Thanks in advance,

Marla

```html
<!DOCTYPE html>
<html lang="en">
<head>
<meta charset="utf-8">
<title>Amber Vela Business Card</title>
<link href="https://fonts.googleapis.com/css2?family=Open+Sans:wght@400;600&display=swap" rel="stylesheet">
<style>
  :root {
    --backdrop: #5a5a5a;
    --card-white: #ffffff;
    --gold: #b8955f;
    --gold-light: #d9bf93;
    --gold-deep: #b6976b;
    --ink: #1e1e1e;
    --icon: #b39a78;
    --divider: #8a8a8a;
  }
  * { margin: 0; padding: 0; box-sizing: border-box; }
  html, body { width: 1200px; height: 802px; overflow: hidden; }
  body {
    background: var(--backdrop);
    font-family: "Open Sans", sans-serif;
    position: relative;
  }
  .card {
    position: absolute;
    top: 274px;
    width: 442px;
    height: 265px;
    box-shadow: 0 3px 8px rgba(0,0,0,0.45);
  }
  .card--front { left: 136px; background: var(--card-white); }
  .card--back {
    left: 624px;
    background: radial-gradient(ellipse at 45% 40%, var(--gold-light) 0%, #c9aa7c 45%, var(--gold-deep) 100%);
  }
  .brand-mark {
    position: absolute;
    left: 44px;
    top: 60px;
    width: 150px;
    text-align: center;
  }
  .brand-mark__dot {
    width: 96px;
    height: 96px;
    border-radius: 50%;
    background: var(--gold);
    margin: 0 auto 18px;
  }
  .brand-mark__name {
    font-weight: 600;
    font-size: 17px;
    color: var(--gold);
    letter-spacing: 0.3px;
    white-space: nowrap;
  }
  .divider {
    position: absolute;
    left: 210px;
    top: 79px;
    width: 1px;
    height: 111px;
    background: var(--divider);
  }
  .contact { position: absolute; left: 236px; top: 74px; }
  .contact__name {
    font-weight: 600;
    font-size: 15px;
    color: var(--gold);
    letter-spacing: 0.2px;
    line-height: 18px;
  }
  .contact__role { font-size: 12.5px; color: var(--ink); line-height: 16px; }
  .contact__list { list-style: none; margin-top: 16px; }
  .contact__item {
    display: flex;
    align-items: center;
    font-size: 12.5px;
    color: var(--ink);
    line-height: 15.6px;
  }
  .contact__icon { width: 9px; height: 9px; margin-right: 6px; fill: var(--icon); }
  .back-name {
    position: absolute;
    left: 300px;
    top: 161px;
    width: 100px;
    text-align: center;
    font-weight: 600;
    font-size: 13px;
    color: var(--card-white);
    letter-spacing: 0.3px;
  }
</style>
</head>
<body>
  <section class="card card--front">
    <div class="brand-mark">
      <div class="brand-mark__dot"></div>
      <div class="brand-mark__name">AMBER VELA</div>
    </div>
    <div class="divider"></div>
    <div class="contact">
      <div class="contact__name">MARLA DUNMORE</div>
      <div class="contact__role">CEO</div>
      <ul class="contact__list">
        <li class="contact__item">
          <svg class="contact__icon" viewBox="0 0 10 10"><path d="M0 4 Q5 0 10 4 L8 5 L7 3.5 L3 3.5 L2 5 Z M2 6 H8 V9 H2 Z"/></svg>
          1(888) 555-0142
        </li>
        <li class="contact__item">
          <svg class="contact__icon" viewBox="0 0 10 10"><path d="M3 0 H7 V10 H3 Z M3.8 1 V8 H6.2 V1 Z"/></svg>
          1(347) 555-0187
        </li>
        <li class="contact__item">
          <svg class="contact__icon" viewBox="0 0 10 10"><path d="M0 2 H10 V8 H0 Z" /><path d="M0 2 L5 5.5 L10 2" fill="none" stroke="#fff" stroke-width="0.8"/></svg>
          marla@loveambervela.com
        </li>
        <li class="contact__item">
          <svg class="contact__icon" viewBox="0 0 10 10"><circle cx="5" cy="5" r="4.6"/><path d="M0.5 5 H9.5 M5 0.5 V9.5" stroke="#fff" stroke-width="0.6"/></svg>
          www.loveambervela.com
        </li>
      </ul>
    </div>
  </section>

  <section class="card card--back" role="img" aria-label="Gold foil background with a faint repeating floral pattern">
    <div class="back-name">AMBER VELA</div>
  </section>
</body>
</html>
```